Family Owned Construction Company Needs Modern Business Cards

We need a new design for our business cards. We are a family owned construction company, Brantwell Construction, based in Mendon, Vermont and would like to add in our new logo and find a more modern look. We also want to use our old to make sure people know who we are. We do site development, highway, environmental, demolition, utility and aggregate.

Contact Information for Business Card

We want to have the office address, 418 Quarry Ridge Road, Alder Falls, VT 05788 and our phone (802) 555-0137 and fax (802) 555-0164 on there as well. Our website is www.brantwellinc.example. There should be a place for the person's name, title, cell number, and email address on the card. Words that we would like to be associated with our company are honesty, predictable, reliable, integrity, dedicated, built right quality, consistent, whatever it takes, and innovation. Safety is also very important to us.

Font styles to use
Serif
Sans Serif
Other font styles liked:
• Square 721 Extented

Colors
0255a3
ffffff

Requirements
Must have
• Office address, phone number and fax number. New logo with excavator
Nice to have
• That we do site development, highway, environmental, demolition, utility, and aggregate. Both logos

```html
<!DOCTYPE html>
<html lang="en">
<head>
<meta charset="utf-8">
<title>Brantwell Construction – Business Cards</title>
<link rel="stylesheet" href="https://fonts.googleapis.com/css2?family=Michroma&family=Roboto+Condensed:wght@400;700&display=swap">
<style>
  :root {
    --brand-blue: #0255a3;
    --deep-blue: #023f7c;
    --white: #ffffff;
    --band-grey: #6d7077;
    --page-bg: #2a2521;
    --muted-white: rgba(255,255,255,0.85);
  }
  * { box-sizing: border-box; margin: 0; padding: 0; }
  html, body { width: 848px; height: 1200px; overflow: hidden; }
  body {
    background: var(--page-bg);
    font-family: "Roboto Condensed", Arial, sans-serif;
    position: relative;
  }
  .card {
    position: absolute;
    left: 104px;
    width: 640px;
    height: 366px;
    overflow: hidden;
    box-shadow: 0 18px 40px rgba(0,0,0,0.45);
  }
  .card--front {
    top: 150px;
    background: linear-gradient(135deg, var(--brand-blue), var(--deep-blue));
  }
  .card--back { top: 684px; background: var(--brand-blue); }

  .wordmark {
    font-family: "Michroma", Arial, sans-serif;
    font-weight: 400;
    text-transform: uppercase;
    line-height: 1.15;
  }
  .card--front .wordmark {
    position: absolute;
    left: 64px; top: 110px;
    color: var(--white);
    font-size: 46px;
    letter-spacing: 1px;
  }
  .card--front .wordmark .wordmark__sub {
    display: block;
    font-size: 23px;
    letter-spacing: 5px;
    margin-top: 6px;
  }
  .card--front .website {
    position: absolute;
    right: 40px; bottom: 30px;
    color: var(--white);
    font-size: 15px;
    letter-spacing: 1px;
    font-weight: 700;
  }

  .back-shapes { position: absolute; inset: 0; }
  .card--back .wordmark {
    position: absolute;
    left: 30px; top: 214px;
    color: var(--brand-blue);
    font-size: 25px;
  }
  .card--back .wordmark .wordmark__sub {
    display: block;
    font-size: 12.5px;
    letter-spacing: 2.5px;
    margin-top: 4px;
  }
  .contact {
    position: absolute;
    left: 350px; top: 40px;
    color: var(--white);
  }
  .contact__name {
    font-size: 28px; font-weight: 700; letter-spacing: 1.5px;
  }
  .contact__title {
    font-size: 12px; letter-spacing: 3px; text-transform: uppercase;
    color: var(--muted-white); margin-top: 2px; margin-bottom: 22px;
  }
  .contact__list { list-style: none; font-size: 15px; }
  .contact__list li {
    display: flex; align-items: center; gap: 10px; height: 24px;
  }
  .contact__list svg { width: 14px; height: 14px; fill: var(--white); flex: none; }
  .contact__address {
    margin-top: 18px; font-size: 14px; line-height: 1.45; color: var(--muted-white);
  }
  .contact__web {
    margin-top: 12px; font-size: 14px; font-weight: 700; letter-spacing: 1px;
  }
</style>
</head>
<body>

<section class="card card--front" aria-label="Card front">
  <div class="wordmark">Brantwell<span class="wordmark__sub">Construction Inc</span></div>
  <div class="website">www.brantwellinc.example</div>
</section>

<section class="card card--back" aria-label="Card back">
  <svg class="back-shapes" viewBox="0 0 640 366" preserveAspectRatio="none" aria-hidden="true">
    <polygon points="0,0 330,0 270,366 0,366" fill="var(--band-grey)"/>
    <polygon points="0,110 312,110 270,366 0,366" fill="var(--white)"/>
  </svg>
  <div class="wordmark">Brantwell<span class="wordmark__sub">Construction Inc</span></div>

  <div class="contact">
    <div class="contact__name">EVAN MARSH</div>
    <div class="contact__title">Director</div>
    <ul class="contact__list">
      <li><svg viewBox="0 0 24 24"><path d="M6.6 10.8a15 15 0 0 0 6.6 6.6l2.2-2.2c.3-.3.7-.4 1-.2 1.1.4 2.3.6 3.6.6.6 0 1 .4 1 1V20c0 .6-.4 1-1 1A17 17 0 0 1 3 4c0-.6.4-1 1-1h3.5c.6 0 1 .4 1 1 0 1.3.2 2.5.6 3.6.1.3 0 .7-.2 1z"/></svg>(802) 555-0137</li>
      <li><svg viewBox="0 0 24 24"><path d="M6 2h9l3 3v5H6zM4 11h16a2 2 0 0 1 2 2v7H2v-7a2 2 0 0 1 2-2zm13 3a1 1 0 1 0 0 2 1 1 0 0 0 0-2z"/></svg>(802) 555-0164</li>
      <li><svg viewBox="0 0 24 24"><path d="M7 1h10a2 2 0 0 1 2 2v18a2 2 0 0 1-2 2H7a2 2 0 0 1-2-2V3a2 2 0 0 1 2-2zm0 3v14h10V4zm5 15.5a1 1 0 1 0 0 2 1 1 0 0 0 0-2z"/></svg>(802) 555-0191</li>
      <li><svg viewBox="0 0 24 24"><path d="M2 5h20v14H2zm2 2v.5l8 5 8-5V7l-8 5z"/></svg>evan@brantwellinc.example</li>
    </ul>
    <div class="contact__address">418 Quarry Ridge Road<br>Alder Falls, VT 05788</div>
    <div class="contact__web">www.brantwellinc.example</div>
  </div>
</section>

</body>
</html>
```